Poster for Office

Looking for an edgy, beautiful poster to hang up in my office that uses the quotes located below and potentially the image attached.
Content for poster

Title: Pell's Rules

Must have the following quotes included (punctuation and capitalization are flexible, do what you think looks the best they also don't need the quotation symbols):

"Don't order fish at a steakhouse"
"Be bold. The more you tell, the more you sell"
"admit nothing, deny everything, launch counterattack."
"avoid obviousness"
"never do anything until you're ready to do it"
"look good=feel good"
"always keep the advantage"
"never complain, never explain"
"Lay low, play dumb, keep moving"

Industry/Entity Type

Quotes

Requirements
Must have
• Title: Pell's Rules

"avoid obviousness"
"look good=feel good"

```html
<!DOCTYPE html>
<html lang="en">
<head>
<meta charset="utf-8">
<title>Pell's Rules</title>
<link rel="stylesheet" href="https://fonts.googleapis.com/css2?family=Special+Elite&family=Jura:wght@600;700&display=swap">
<style>
  :root {
    --paper: #c6c6c6;
    --paper-light: #d6d6d6;
    --paper-dark: #9a9a9a;
    --ink: #1c1c1c;
    --tile: #151515;
    --tile-text: #dcdcdc;
    --figure-light: #b4b4b4;
    --figure-dark: #7d7d7d;
  }
  * { margin: 0; padding: 0; box-sizing: border-box; }
  html, body {
    width: 848px;
    height: 1200px;
    overflow: hidden;
    background: var(--paper);
  }
  .poster {
    position: relative;
    width: 848px;
    height: 1200px;
    overflow: hidden;
    background:
      radial-gradient(ellipse at 15% 10%, var(--paper-dark) 0%, transparent 35%),
      radial-gradient(ellipse at 80% 75%, rgba(120,120,120,0.45) 0%, transparent 40%),
      radial-gradient(ellipse at 60% 30%, var(--paper-light) 0%, transparent 45%),
      radial-gradient(ellipse at 30% 95%, rgba(140,140,140,0.5) 0%, transparent 40%),
      var(--paper);
  }
  .figure-photo {
    position: absolute;
    left: 0;
    top: 270px;
    width: 500px;
    height: 850px;
    background:
      radial-gradient(ellipse at 35% 12%, var(--figure-dark) 0%, transparent 30%),
      radial-gradient(ellipse at 45% 50%, var(--figure-light) 0%, transparent 70%);
    opacity: 0.8;
  }
  .title {
    position: absolute;
    top: 112px;
    left: 0;
    width: 848px;
    display: flex;
    justify-content: center;
    gap: 4px;
    font-family: "Special Elite", serif;
    font-size: 38px;
    line-height: 1;
  }
  .title .tile {
    display: inline-block;
    width: 40px;
    height: 46px;
    padding-top: 5px;
    text-align: center;
    background: var(--tile);
    color: var(--tile-text);
    border-radius: 6px 3px 7px 4px;
  }
  .title .gap { width: 26px; }
  .title .mark {
    width: 16px;
    color: var(--tile);
    text-align: center;
  }
  .rules {
    position: absolute;
    right: 48px;
    top: 308px;
    list-style: none;
    text-align: right;
    font-family: "Jura", sans-serif;
    font-weight: 700;
    font-size: 22px;
    color: var(--ink);
    letter-spacing: 0.3px;
  }
  .rules li {
    height: 84.5px;
    text-shadow: 1px 1px 1px rgba(0,0,0,0.25);
  }
  .corner { position: absolute; }
</style>
</head>
<body>
<div class="poster">
  <div class="figure-photo" role="img" aria-label="Faded black-and-white photograph of a man's bare back, seen from behind, with a portrait tattoo between his shoulders"></div>

  <h1 class="title" aria-label="Pell's Rules">
    <span class="tile">P</span><span class="tile">E</span><span class="tile">L</span><span class="tile">L</span><span class="mark">'</span><span class="tile">S</span>
    <span class="gap"></span>
    <span class="tile">R</span><span class="tile">U</span><span class="tile">L</span><span class="tile">E</span><span class="tile">S</span>
  </h1>

  <svg class="corner" style="left:0;top:0" width="848" height="1200" viewBox="0 0 848 1200" aria-hidden="true">
    <g stroke="#111" stroke-width="3">
      <line x1="32" y1="226" x2="32" y2="278"/>
      <line x1="57" y1="227" x2="108" y2="227"/>
      <line x1="825" y1="1050" x2="825" y2="1100"/>
      <line x1="749" y1="1098" x2="801" y2="1098"/>
    </g>
  </svg>

  <ul class="rules">
    <li>"Don't order fish at a steakhouse"</li>
    <li>"Be bold. The more you tell, the more you sell"</li>
    <li>"Admit nothing, deny everything, launch counterattack."</li>
    <li>"Avoid obviousness"</li>
    <li>"Never do anything until you're ready to do it"</li>
    <li>"Look good=feel good"</li>
    <li>"Always keep the advantage"</li>
    <li>"Never complain, never explain"</li>
    <li>"Lay low, play dumb, keep moving"</li>
  </ul>
</div>
</body>
</html>
```